Outdoor sign for Brindle Auto Restoration

I need a horizontal 4'x 8' outdoor roadside sign for my classic auto restoration business. I have uploaded colors and our logo. Needs the Brindle name, a prominent Classic AUTO RESTORATION, phone number and website. We rebuild and restore vintage cars, trucks and 4x4s. I'd like something clean but possibly retro. Classic Auto Restoration is more important than the Brindle name. It needs to be visible and readable from the street. NO CLIP ART

Target Market(s)

Customers who need their vintage care restored or upgraded. Men and women ages 25-75

Industry/Entity Type

Automotive

Colors
FFC000
F8CF3A
FAE287
FDF2CF
FEFAEE

Requirements
Must have
• Legible. Bright. Readable as a backlit 4' x 8' large horizontal sign (roughly 120cm X 240cm)
Nice to have
• Use of the Brindle logo/type, Complete or Classic before prominent AUTO RESTORATION
Should not have
• Clip art of old cars or icons. And we don't want the Brindle Logo from the website because it wont be legible from the road. I have included the Illustrator file for Brindle text in the uploads

```html
<!DOCTYPE html>
<html lang="en">
<head>
<meta charset="utf-8">
<title>Brindle Auto Restoration – Roadside Sign</title>
<link rel="stylesheet" href="https://fonts.googleapis.com/css2?family=Anton&family=Roboto+Condensed:wght@700&family=Yellowtail&display=swap">
<style>
  :root {
    --sign-black: #231f20;
    --sign-gold: #f8b01a;
  }
  html, body {
    margin: 0;
    padding: 0;
    width: 1200px;
    height: 600px;
    overflow: hidden;
    background: var(--sign-black);
  }
  .sign {
    display: block;
    width: 1200px;
    height: 600px;
    background: var(--sign-black);
  }
  .tagline-script {
    font-family: "Yellowtail", cursive;
    font-size: 124px;
    fill: var(--sign-gold);
  }
  .headline {
    font-family: "Anton", sans-serif;
    font-size: 152px;
  }
  .headline-face { fill: var(--sign-gold); }
  .headline-shadow {
    fill: var(--sign-black);
    stroke: var(--sign-gold);
    stroke-width: 1.2px;
  }
  .business-name {
    font-family: "Roboto Condensed", sans-serif;
    font-weight: 700;
    font-size: 68px;
    fill: var(--sign-gold);
  }
  .contact-text {
    font-family: "Roboto Condensed", sans-serif;
    font-weight: 700;
    font-size: 47px;
    fill: var(--sign-gold);
  }
  .icon-fill { fill: var(--sign-gold); }
  .icon-line {
    fill: none;
    stroke: var(--sign-gold);
    stroke-width: 3px;
  }
</style>
</head>
<body>
<svg class="sign" viewBox="0 0 1200 600" xmlns="http://www.w3.org/2000/svg" role="img" aria-label="Classic Auto Restoration – Brindle – 501-555-0148 – brindleautoshop.com">
  <text class="tagline-script" x="600" y="158" text-anchor="middle">Classic</text>

  <g class="headline">
    <text class="headline-shadow" x="96" y="339" textLength="1008" lengthAdjust="spacingAndGlyphs">AUTO RESTORATION</text>
    <text class="headline-face" x="96" y="331" textLength="1008" lengthAdjust="spacingAndGlyphs">AUTO RESTORATION</text>
  </g>

  <text class="business-name" x="600" y="430" text-anchor="middle">BRINDLE</text>

  <g class="contact-phone">
    <path class="icon-fill" d="M170 478 c-8 0 -13 10 -13 21 c0 11 5 21 13 21 l6 0 c3 0 4 -3 3 -5 l-3 -4 c-2 -2 -5 -1 -6 1 c-4 -3 -5 -9 -5 -13 c0 -4 1 -10 5 -13 c1 2 4 3 6 1 l3 -4 c1 -2 0 -5 -3 -5 z"/>
    <text class="contact-text" x="189" y="515">501-555-0148</text>
  </g>

  <g class="contact-web">
    <g class="globe-icon">
      <circle class="icon-line" cx="529" cy="499" r="20"/>
      <ellipse class="icon-line" cx="529" cy="499" rx="9" ry="20"/>
      <line class="icon-line" x1="529" y1="479" x2="529" y2="519"/>
      <line class="icon-line" x1="509" y1="499" x2="549" y2="499"/>
      <line class="icon-line" x1="513" y1="488" x2="545" y2="488"/>
      <line class="icon-line" x1="513" y1="510" x2="545" y2="510"/>
    </g>
    <text class="contact-text" x="564" y="515" textLength="480" lengthAdjust="spacingAndGlyphs">BRINDLEAUTOSHOP.COM</text>
  </g>
</svg>
</body>
</html>
```